Long term design collaboration - mobile app design & web app design

We are looking for a talented mobile designer to help us improve our UI & UX for mobile app and web app.

The screens that need to be redesigned are attached.

There is potentially a lot more work in future design available for the successful candidate.
The successful candidate would have to take part in daily stand-up around 3 times per week.
The successful candidate would join a dev team
We are software company that does property management

```html
<!DOCTYPE html>
<html lang="en">
<head>
<meta charset="utf-8">
<title>Larvo – Overview</title>
<link href="https://fonts.googleapis.com/css2?family=Inter:wght@400;500;600&family=Poppins:wght@500;600&display=swap" rel="stylesheet">
<style>
:root{
  --bg:#f4f5f9;
  --white:#ffffff;
  --primary:#1a16f0;
  --violet:#4f4aec;
  --coral:#ff5b73;
  --ink:#1e1f24;
  --muted:#9a9a9e;
  --value:#5b72b8;
  --warn-bg:#f6ead5;
  --warn:#fbb833;
  --line:#e4e7ef;
  --chip:#e8edfb;
}
*{box-sizing:border-box;margin:0;padding:0}
html,body{width:1200px;height:1140px;overflow:hidden}
body{background:var(--bg);font-family:"Inter",sans-serif;color:var(--ink);position:relative}
.abs{position:absolute}
.topbar{left:0;top:0;width:1200px;height:80px;background:var(--white)}
.close-icon{left:22px;top:22px}
.brand{left:123px;top:18px;font-family:"Poppins",sans-serif;font-weight:600;font-size:34px;color:var(--primary);line-height:44px}
.avatar{left:338px;top:16px;width:48px;height:48px;border-radius:50%;background:radial-gradient(circle at 50% 40%,#c9a68c,#3e5a55)}
.user-name{left:400px;top:20px;font-weight:600;font-size:22px;line-height:26px}
.user-link{left:400px;top:45px;font-size:14px;color:var(--value)}
.bell{left:1120px;top:24px}
.sidebar{left:22px;top:103px;width:293px;height:1014px;background:var(--white);border-radius:22px}
.nav-item{left:74px;font-family:"Poppins",sans-serif;font-weight:500;font-size:20px;color:var(--muted);line-height:28px}
.nav-active{left:45px;top:355px;width:248px;height:56px;border-radius:8px;background:var(--primary)}
.nav-item.active{color:var(--white);font-weight:600}
.btn{display:flex;align-items:center;justify-content:center;color:var(--white);font-size:18px;border-radius:7px}
.logout{left:45px;top:1039px;width:248px;height:56px;background:var(--coral);font-family:"Poppins",sans-serif;font-weight:600;font-size:20px}
.h-title{left:340px;font-weight:500;font-size:22px;line-height:28px}
.report{left:1003px;top:151px;width:150px;height:46px;background:var(--primary)}
.setup{left:339px;top:221px;width:814px;height:210px;background:var(--warn-bg);border:2px solid var(--warn);border-radius:22px}
.setup-title{left:372px;top:246px;font-weight:600;font-size:20px}
.setup-item{left:372px;font-size:16px;color:#858585;line-height:20px}
.warn-arrow{left:1103px}
.summary{left:338px;top:454px;width:150px;height:47px;background:var(--primary)}
.detail{left:515px;top:454px;width:149px;height:47px;background:var(--coral)}
.card{background:var(--white);border-radius:22px}
.general{left:339px;top:572px;width:814px;height:200px}
.row-label{left:377px;font-size:16px;line-height:20px}
.row-value{left:580px;font-size:16px;line-height:20px;color:var(--value)}
.divider{left:377px;width:738px;height:1px;background:var(--line)}
.go{left:1088px;width:28px;height:28px;border-radius:7px;background:var(--chip);display:flex;align-items:center;justify-content:center}
.comp{top:843px;height:107px;border-radius:24px;background:var(--white)}
.comp-name{font-size:16px;line-height:20px}
.comp-val{font-size:12px;line-height:15px;color:var(--value)}
.comp.solid{background:var(--primary)}
.comp.soft{background:var(--violet)}
.comp.solid .comp-name,.comp.soft .comp-name{color:var(--white)}
.comp.solid .comp-val,.comp.soft .comp-val{color:#c9ccff}
.insurance{left:339px;top:1024px;width:814px;height:83px}
.ins-icon{left:354px;top:1039px;width:55px;height:55px;border-radius:16px;background:var(--chip);display:flex;align-items:center;justify-content:center}
.ins-name{top:1044px;font-size:16px;line-height:20px}
.ins-val{top:1068px;font-size:15px;line-height:20px;color:var(--value)}
</style>
</head>
<body>
<header class="abs topbar"></header>
<svg class="abs close-icon" width="38" height="38" viewBox="0 0 38 38" aria-label="Close"><circle cx="19" cy="19" r="17" fill="none" stroke="#1a16f0" stroke-width="3"/><path d="M13 13l12 12M25 13L13 25" stroke="#1a16f0" stroke-width="3" stroke-linecap="round"/></svg>
<div class="abs brand">Larvo</div>
<div class="abs avatar" role="img" aria-label="Profile photo of the account holder"></div>
<div class="abs user-name">Marisa Holden</div>
<div class="abs user-link">My account</div>
<svg class="abs bell" width="30" height="34" viewBox="0 0 30 34" aria-label="Notifications"><path d="M14 4c-6 0-9 4-9 10v6l-4 5h26l-4-5v-6c0-6-3-10-9-10z" fill="#1a16f0"/><rect x="10" y="27" width="8" height="4" rx="2" fill="#1a16f0"/><circle cx="24" cy="6" r="5" fill="#1a16f0" stroke="#fff" stroke-width="2"/></svg>

<aside class="abs sidebar"></aside>
<div class="abs nav-item" style="top:145px">User Directory</div>
<div class="abs nav-item" style="top:202px">Switch Development</div>
<div class="abs nav-item" style="top:258px">Services Change</div>
<div class="abs nav-item" style="top:314px">Propery Balance</div>
<div class="abs nav-active"></div>
<div class="abs nav-item active" style="top:370px">Sending Letter</div>
<div class="abs nav-item" style="top:426px">Reguler Services</div>
<div class="abs btn logout">Log out</div>

<div class="abs h-title" style="top:148px;left:343px">Overview</div>
<div class="abs btn report">Report</div>

<section class="abs setup"></section>
<div class="abs setup-title">Please complete basic setup</div>
<div class="abs setup-item" style="top:290px">Service Charge Schedules</div>
<div class="abs setup-item" style="top:320px">Service Charge Apportionment</div>
<div class="abs setup-item" style="top:350px">Invite resident &amp; leaseholders</div>
<div class="abs setup-item" style="top:380px">Connect payament provider</div>
<svg class="abs warn-arrow" style="top:287px" width="16" height="12" viewBox="0 0 16 12"><path d="M1 6h13M9 1l5 5-5 5" fill="none" stroke="#fbb833" stroke-width="2"/></svg>
<svg class="abs warn-arrow" style="top:312px" width="16" height="12" viewBox="0 0 16 12"><path d="M1 6h13M9 1l5 5-5 5" fill="none" stroke="#fbb833" stroke-width="2"/></svg>
<svg class="abs warn-arrow" style="top:337px" width="16" height="12" viewBox="0 0 16 12"><path d="M1 6h13M9 1l5 5-5 5" fill="none" stroke="#fbb833" stroke-width="2"/></svg>
<svg class="abs warn-arrow" style="top:361px" width="16" height="12" viewBox="0 0 16 12"><path d="M1 6h13M9 1l5 5-5 5" fill="none" stroke="#fbb833" stroke-width="2"/></svg>
<svg class="abs warn-arrow" style="top:386px" width="16" height="12" viewBox="0 0 16 12"><path d="M1 6h13M9 1l5 5-5 5" fill="none" stroke="#fbb833" stroke-width="2"/></svg>

<div class="abs btn summary">Summary</div>
<div class="abs btn detail">Detail</div>

<div class="abs h-title" style="top:524px">General</div>
<section class="abs card general"></section>
<div class="abs row-label" style="top:598px">Unit</div><div class="abs row-value" style="top:598px">85</div>
<div class="abs divider" style="top:628px"></div>
<div class="abs row-label" style="top:638px">Handover Date</div><div class="abs row-value" style="top:638px">12 Januari 2023</div>
<div class="abs divider" style="top:668px"></div>
<div class="abs row-label" style="top:679px">Address</div><div class="abs row-value" style="top:679px">42 Fenwick Crescent, London, W12 8QT</div>
<div class="abs divider" style="top:708px"></div>
<div class="abs row-label" style="top:719px">Sections 20 limit</div><div class="abs row-value" style="top:719px">$20</div>
<div class="abs go" style="top:594px"><svg width="14" height="10" viewBox="0 0 14 10"><path d="M1 5h11M8 1l4 4-4 4" fill="none" stroke="#1a16f0" stroke-width="2"/></svg></div>
<div class="abs go" style="top:634px"><svg width="14" height="10" viewBox="0 0 14 10"><path d="M1 5h11M8 1l4 4-4 4" fill="none" stroke="#1a16f0" stroke-width="2"/></svg></div>
<div class="abs go" style="top:675px"><svg width="14" height="10" viewBox="0 0 14 10"><path d="M1 5h11M8 1l4 4-4 4" fill="none" stroke="#1a16f0" stroke-width="2"/></svg></div>
<div class="abs go" style="top:715px"><svg width="14" height="10" viewBox="0 0 14 10"><path d="M1 5h11M8 1l4 4-4 4" fill="none" stroke="#1a16f0" stroke-width="2"/></svg></div>

<div class="abs h-title" style="top:794px">Compliance</div>
<div class="abs comp" style="left:339px;width:144px"></div>
<div class="abs comp" style="left:507px;width:167px"></div>
<div class="abs comp" style="left:698px;width:167px"></div>
<div class="abs comp solid" style="left:889px;width:107px"></div>
<div class="abs comp soft" style="left:1021px;width:132px"></div>
<div class="abs comp-name" style="left:377px;top:867px">Asbetsos</div><div class="abs comp-val" style="left:379px;top:901px">NA</div>
<div class="abs comp-name" style="left:535px;top:867px">Legionellas</div><div class="abs comp-val" style="left:537px;top:901px">-</div>
<div class="abs comp-name" style="left:725px;top:867px">Drains</div><div class="abs comp-val" style="left:727px;top:901px">Overdue<br>10 December 2023</div>
<div class="abs comp-name" style="left:916px;top:867px;color:#fff">Gutters</div><div class="abs comp-val" style="left:918px;top:901px;color:#c9ccff">NA</div>
<div class="abs comp-name" style="left:1047px;top:867px;color:#fff">Dry Rises</div><div class="abs comp-val" style="left:1049px;top:901px;color:#c9ccff">NA</div>

<div class="abs h-title" style="top:972px">Issurance</div>
<section class="abs card insurance"></section>
<div class="abs ins-icon"><svg width="26" height="20" viewBox="0 0 26 20"><rect x="1" y="2" width="19" height="13" rx="2" fill="#1a16f0"/><rect x="1" y="5" width="19" height="2" fill="#e8edfb"/><rect x="4" y="10" width="6" height="2" fill="#e8edfb"/><circle cx="20" cy="14" r="5" fill="#1a16f0" stroke="#e8edfb" stroke-width="1.5"/><path d="M20 11v6" stroke="#fff" stroke-width="1.2"/></svg></div>
<div class="abs ins-name" style="left:430px">Terrorism</div><div class="abs ins-val" style="left:430px">NA</div>
<div class="abs ins-name" style="left:544px">Buildings</div><div class="abs ins-val" style="left:544px">NA</div>
<div class="abs ins-name" style="left:650px">Enggnering</div><div class="abs ins-val" style="left:650px">NA</div>
<div class="abs ins-name" style="left:793px">D &amp; O</div><div class="abs ins-val" style="left:793px">NA</div>
<div class="abs ins-name" style="left:882px">Reinstatemen</div><div class="abs ins-val" style="left:882px">NA</div>
</body>
</html>
```